Therapeutic Counselling Practice Brochure

I have a new therapeutic counselling practice in Melbourne.

I am making peri natal issues my special interest area.

I need a brochure targeted at new parents or pregnant women and partners, struggling with the concept of parenting, depression, maybe do not even know about it.

The feel should be safe and strong. I love the KOALIN website ( I do volunteer work with them)

Out of hours appointments and telephone counselling are important making my service very accessible.

Attached is an example for the content of the Brochure
Updates

Attached is an example for the content of the Brochure.

Target Market(s)

25 - 45 New Parents , expectant parents,families and friends of people struggling emotionally and mentally with and around being new parents

Industry/Entity Type

Work

Requirements
Must have
• Feel of safety, somewhere to go for help, support, a conversation, soft ,strong
Nice to have
• mother and child, maybe parents and child, possibly a graphic, faceless

```html
<!DOCTYPE html>
<html lang="en">
<head>
<meta charset="utf-8">
<title>Miriam Ashcombe J.P. – Counselling</title>
<link rel="stylesheet" href="https://fonts.googleapis.com/css2?family=Cabin:ital,wght@0,400;0,700;1,400;1,700&display=swap">
<style>
  :root {
    --ink: #2e2e2e;
    --name-green: #1f3a12;
    --leaf: #8dc63f;
    --leaf-dark: #6fae2a;
    --leaf-pale: #d9ecc0;
    --band-pale: #eef6e2;
    --paper: #ffffff;
  }
  html, body {
    margin: 0;
    padding: 0;
    width: 1200px;
    height: 2479px;
    overflow: hidden;
    background: var(--paper);
  }
  .brochure {
    position: relative;
    width: 1200px;
    height: 2479px;
    overflow: hidden;
    background: var(--paper);
    font-family: "Cabin", "Trebuchet MS", sans-serif;
    color: var(--ink);
  }
  .portrait {
    position: absolute;
    left: 0; top: 0;
    width: 1200px; height: 830px;
    background:
      radial-gradient(ellipse at 40% 40%, #f3ede6 0%, #e7dccf 30%, transparent 55%),
      linear-gradient(120deg, #f4f6ee 0%, #d9e8c4 45%, #8fb45a 75%, #4f7a2a 100%);
  }
  .name-band {
    position: absolute;
    left: 0; top: 756px;
    width: 1200px; height: 117px;
    background: linear-gradient(90deg, var(--band-pale) 0%, rgba(238,246,226,0.95) 55%, rgba(238,246,226,0) 100%);
  }
  .name-wedge {
    position: absolute;
    left: 0; top: 763px;
    width: 112px; height: 159px;
  }
  .practitioner-name {
    position: absolute;
    left: 186px; top: 772px;
    margin: 0;
    font-size: 60px;
    line-height: 78px;
    font-weight: 700;
    color: var(--name-green);
    white-space: nowrap;
  }
  .block {
    position: absolute;
    left: 131px;
    width: 940px;
    margin: 0;
    font-size: 44px;
    line-height: 60px;
  }
  .block .line { display: block; white-space: nowrap; }
  .block .fill {
    text-align: justify;
    text-align-last: justify;
  }
  .office { top: 969px; }
  .office strong { font-weight: 700; }
  .hours { top: 1150px; font-style: italic; }
  .phone-intro { top: 1267px; }
  .phone-intro strong { font-weight: 700; }
  .convenience { top: 1443px; }
  .comfort { top: 1619px; }
  .highlight {
    position: absolute;
    left: 100px; top: 1853px;
    width: 1000px;
    margin: 0;
    text-align: center;
    font-size: 50px;
    line-height: 62px;
    font-weight: 700;
    font-style: italic;
  }
  .booking {
    position: absolute;
    left: 100px; top: 1994px;
    width: 1000px;
    text-align: center;
    font-size: 44px;
    line-height: 59px;
  }
  .booking p { margin: 0; white-space: nowrap; }
  .booking .bold { font-weight: 700; font-size: 46px; }
  .footer-swoosh {
    position: absolute;
    left: 0; top: 2300px;
    width: 1200px; height: 179px;
  }
</style>
</head>
<body>
<main class="brochure">
  <div class="portrait" role="img" aria-label="Portrait photograph of the counsellor smiling among soft green leafy plants"></div>

  <div class="name-band"></div>
  <svg class="name-wedge" viewBox="0 0 112 159" aria-hidden="true">
    <polygon points="0,0 112,0 0,159" fill="var(--leaf)"/>
  </svg>
  <h1 class="practitioner-name">Miriam Ashcombe J.P.</h1>

  <p class="block office">
    <span class="line"><strong>Office:</strong></span>
    <span class="line">Level 1, 42 Harrow Lane,</span>
    <span class="line">Eastwood Park 3108</span>
  </p>

  <p class="block hours"><span class="line">Evening and weekend appointments available.</span></p>

  <p class="block phone-intro">
    <span class="line fill"><strong>Telephone Counselling</strong> saves travel time and</span>
    <span class="line">the hassle of parking.</span>
  </p>

  <p class="block convenience">
    <span class="line fill">Telephone counselling gives you a convenient</span>
    <span class="line">option in accessing therapy.</span>
  </p>

  <p class="block comfort">
    <span class="line fill">Some people feel more comfortable discussing</span>
    <span class="line fill">issues over the telephone, still within the safe</span>
    <span class="line">supportive and confidential framework.</span>
  </p>

  <p class="highlight">Telephone appointments are usually<br>available within 48 hours.</p>

  <section class="booking">
    <p>To book please contact</p>
    <p class="bold">Miriam Ashcombe</p>
    <p>on <span class="bold">&nbsp;0400 555 318</span></p>
    <p class="bold">miriam@miriamashcombe.com.au</p>
    <p class="bold">www.miriamashcombe.com.au</p>
  </section>

  <svg class="footer-swoosh" viewBox="0 0 1200 179" preserveAspectRatio="none" aria-hidden="true">
    <defs>
      <linearGradient id="swoosh-pale" x1="0" y1="0" x2="1" y2="0">
        <stop offset="0" stop-color="var(--leaf-pale)" stop-opacity="0.4"/>
        <stop offset="1" stop-color="var(--leaf-pale)"/>
      </linearGradient>
      <linearGradient id="swoosh-main" x1="0" y1="0" x2="1" y2="0">
        <stop offset="0" stop-color="var(--leaf)"/>
        <stop offset="1" stop-color="var(--leaf-dark)"/>
      </linearGradient>
    </defs>
    <path d="M80,30 C500,55 900,40 1200,0 L1200,179 L0,179 Z" fill="url(#swoosh-pale)"/>
    <path d="M0,70 C400,80 850,65 1200,30 L1200,179 L0,179 Z" fill="url(#swoosh-main)"/>
  </svg>
</main>
</body>
</html>
```